Company Business Card (Company Promotions)

We want a Business Card that is both Elegant & High Class. We want the card stock thick and unique. We want it to build our Brand Name. We service Automobile dealerships & owners who drive luxury & exotic automobiles that cost an average of $75K. We provide towing services for Luxury & Exotic vehicles. Our colors are Black & Construction Yellow (Gold).
We are manufacture certified for Varenholt Kress, QRT, DULO, EKVA, Lindgard, HK, Calvetti, Tolvenor, Castroviallo, Oryth & Solvance. We have authorization to use their logo's.
Enclosed is our old business card. We only used the unusual & Unique brands on the cards but are open to the use of all of them. We also use the Federal Competence Badge that identifies our abilities.

Also enclosed is the name font that we use.

Target Market(s)

Business, Executive, Hi end people that drive finer luxury &/or exotic automobiles.

Industry/Entity Type

Business

Contact Information for Business Card

We market our name. Haul Meridian. Business address is: 8142 Birchfield Avenue, NE Ste: 212, Atlanta, GA 30309 Phone: 404-555-0183. Web address is hmhaul.example
Manufacture Certified / Nationally Certified

Font styles to use
Other font styles liked:
• AR DESTINE (in Italic's)

Colors
ffc214

Requirements
Must have
• Must have the at least 5 of the manufacture logo's and the Federal Guild Logo (see on other business card)
Nice to have
• Place the manfacture logo's on the back.
Should not have
• No other colors than Black, Yellow & White

```html
<!DOCTYPE html>
<html lang="en">
<head>
<meta charset="utf-8">
<title>Haul Meridian – Business Card</title>
<link rel="stylesheet" href="https://fonts.googleapis.com/css2?family=Arvo:wght@700&display=swap">
<style>
  :root {
    --yellow: #ffc214;
    --black: #0b0b0b;
    --carbon-a: #1c1c1c;
    --carbon-b: #2b2b2b;
    --white: #f7f7f5;
    --stage: #e4e4e2;
    --badge: #3a3a3a;
    --badge-light: #ece8dc;
  }
  * { box-sizing: border-box; margin: 0; padding: 0; }
  html, body { width: 1200px; height: 864px; overflow: hidden; }
  body {
    background: var(--stage);
    font-family: "Arvo", Georgia, serif;
    font-weight: 700;
    display: flex;
    align-items: center;
    justify-content: center;
    gap: 40px;
  }
  .card {
    position: relative;
    width: 560px;
    height: 320px;
    overflow: hidden;
    box-shadow: 0 6px 18px rgba(0,0,0,0.25);
  }

  /* ---------- Front ---------- */
  .card--front { background: var(--yellow); }
  .front__top {
    position: absolute; left: 0; top: 0; width: 100%; height: 142px;
    background: linear-gradient(135deg, var(--carbon-b), var(--carbon-a));
  }
  .badge { position: absolute; }
  .front__badge { left: 150px; top: 16px; width: 62px; height: 76px; }
  .brand-name { position: absolute; color: var(--yellow); line-height: 1; }
  .front .brand-name--small, .card--front .brand-name--small { left: 232px; top: 36px; font-size: 22px; }
  .card--front .brand-name--large { left: 262px; top: 58px; font-size: 40px; }
  .rule { position: absolute; height: 2px; background: var(--yellow); }
  .card--front .rule { left: 150px; top: 106px; width: 330px; }
  .tagline {
    position: absolute; left: 150px; top: 114px; width: 330px;
    color: var(--yellow); font-size: 12px; text-align: center; letter-spacing: 0.3px;
  }
  .contact {
    position: absolute; left: 220px; top: 152px;
    color: var(--black); font-size: 16px; line-height: 22px; text-align: center; width: 200px;
  }
  .address {
    position: absolute; left: 30px; top: 226px; width: 500px;
    color: var(--black); font-size: 13.5px; text-align: center;
  }
  .maker-strip {
    position: absolute; left: 0; top: 252px; width: 100%; height: 40px;
    background: var(--white);
    display: flex; align-items: center; justify-content: space-around;
    padding: 0 10px;
  }
  .maker {
    color: var(--black); font-size: 9px; letter-spacing: 0.2px; white-space: nowrap;
  }

  /* ---------- Back ---------- */
  .card--back { background: var(--black); }
  .back__badge { left: 200px; top: 40px; width: 180px; height: 230px; opacity: 0.35; }
  .card--back .brand-name--small { left: 150px; top: 110px; font-size: 28px; }
  .card--back .brand-name--large { left: 220px; top: 138px; font-size: 52px; }
  .card--back .rule { left: 100px; width: 380px; height: 1.5px; top: 124px; }
  .card--back .rule--lower { top: 214px; }
</style>
</head>
<body>

  <section class="card card--front" aria-label="Business card front">
    <div class="front__top" role="img" aria-label="Dark carbon fibre texture"></div>

    <svg class="badge front__badge" viewBox="0 0 62 76" role="img" aria-label="Federal Competence Badge">
      <path d="M4 6 Q31 -2 58 6 L58 40 Q58 62 31 74 Q4 62 4 40 Z" fill="var(--badge-light)" stroke="var(--yellow)" stroke-width="2"/>
    </svg>

    <span class="brand-name brand-name--small">Haul</span>
    <span class="brand-name brand-name--large">Meridian</span>
    <div class="rule"></div>
    <p class="tagline">Manufacture Certified / Nationally Certified</p>

    <p class="contact">404-555-0183<br>404-555-0147<br>hmhaul.example</p>
    <p class="address">8142 Birchfield Avenue, NE Ste: 212, Atlanta, GA 30309</p>

    <div class="maker-strip">
      <span class="maker">Stoneveld</span>
      <span class="maker">QRT</span>
      <span class="maker">Ironmarch</span>
      <span class="maker">Mervane</span>
      <span class="maker">Lindgard</span>
      <span class="maker">Varenholt Kress</span>
      <span class="maker">EKVA</span>
      <span class="maker">Tolvenor</span>
      <span class="maker">Pardline</span>
    </div>
  </section>

  <section class="card card--back" aria-label="Business card back">
    <svg class="badge back__badge" viewBox="0 0 62 76" role="img" aria-label="Faint Federal Competence Badge">
      <path d="M4 6 Q31 -2 58 6 L58 40 Q58 62 31 74 Q4 62 4 40 Z" fill="var(--badge)"/>
    </svg>
    <div class="rule"></div>
    <span class="brand-name brand-name--small">Haul</span>
    <span class="brand-name brand-name--large">Meridian</span>
    <div class="rule rule--lower"></div>
  </section>

</body>
</html>
```